Brivora Distance Learning Website

Brivora provide e-learning and mixed learning solutions for individuals, colleges, organisations and B2B.
We need a modern, light and flat website design for Brivora. We want to to see the designer incorporate user experience(UX) design elements into the AI or PSD mockups. We would like to see designs that use pastel colors that compliment yellow and black of our logo.
We want our E-learning experience to accelerate learning and for the interface to be user friendly and intuitive. We want the designs to focus on quick access to course information, course reviews, learning progress and study advice. Quick and intuitive access to all content for our clients is one of our top priorities.
We would like designs for the following project 3 pages:
1. Learner homepage dashboard (see attached screenshot).
On this page the Learners need to:
- Login
- Have quick access to Packages and Courses.
- See other recommended courses (Below Packages and Courses)
- Possibly a left hand side column/menu with thumbnail icons (See lumivex learner dashboard screenshot)
2. Homepage
See current sample
http://www.brivora-learn.test
We would like the designer to focus on creating a customized banner to enhance the home page.
3. Primary Landing/Marketing page
This page is geared towards customer acquisition with the focal point being the top banner (video or HD image).
And Course Preview content below.
See reference
http://brivora-learn.test/subscriptionPlans/marketing/MTc%3D/Mjc4Nw%3D%3D/Quick%20Fennish%20%2B%20Fennish%20Nibbles%20Bundle%20by%20Harold%20Wen%20Pike
Other site we like:
- https://www.korvanta.test (We like the home page and top bar on courses page)
- http://www.tutorglen.test
- http://crewmapleden.test (think this site looks great, love the lower graphics on the homepage)
Updates
Hello,
Thank you for taking the time to contribute to this web design competition. We would just like to point out a few things:
1. Please try to make the color palette similar to the colors used in the screenshot that we just uploaded ('possible color palette).
2. Please make the designs specific to each page: THE LEARNER HOMEPAGE, HOME PAGE, and the MARKETING LANDING PAGE.
We are very happy with the high quality of designs so far,
Cheers,
Lee Ab
KV-Studio
Also,
Please avoid using dark/bold elements in the designs. The ONLY elements that we want to be dark are the logo and the footer.
Any questions please ask,
Cheers,
Lee Ab
Kv-Studio
Hello,
Based on the round of feedback we just gave it would be great if you could complete further design changes by tomorrow, as we are pushed for time.
Thank you,
Lee Ab
KV-Studio

```html
<!DOCTYPE html>
<html lang="en">
<head>
<meta charset="utf-8">
<title>Brivora – Courses that Work</title>
<link rel="stylesheet" href="https://fonts.googleapis.com/css2?family=PT+Sans:ital,wght@0,400;0,700;1,400;1,700&family=Lato:wght@400;700;900&display=swap">
<style>
:root{
  --yellow:#f7c125;
  --yellow-dark:#e5ad0e;
  --ink:#1b1b1b;
  --text:#333333;
  --muted:#666666;
  --band-grey:#d3d3d3;
  --dark:#333333;
  --darker:#2b2b2b;
  --footer:#cfcfcf;
  --white:#ffffff;
  --line:#c9c9c9;
  --wood-1:#6b4a33;
  --wood-2:#9a7457;
  --wood-3:#4a3324;
}
*{box-sizing:border-box;margin:0;padding:0}
html,body{width:1200px;height:2727px;overflow:hidden}
body{position:relative;font-family:"PT Sans",Arial,sans-serif;color:var(--text);background:var(--white)}
.abs{position:absolute}

/* hero */
.hero{position:absolute;left:0;top:0;width:1200px;height:700px;overflow:hidden}
.hero-photo{position:absolute;inset:0;background:
  linear-gradient(180deg,rgba(0,0,0,.25),rgba(0,0,0,.05) 40%,rgba(0,0,0,.2)),
  linear-gradient(100deg,var(--wood-3),var(--wood-2) 35%,var(--wood-1) 60%,var(--wood-2) 85%,var(--wood-3))}
.brand{position:absolute;left:125px;top:28px;display:flex;align-items:center;gap:12px}
.brand-dot{width:58px;height:58px;border-radius:50%;background:var(--yellow)}
.brand-name{font-size:42px;font-weight:700;color:var(--white);line-height:1}
.brand-tag{position:absolute;left:195px;top:78px;font-size:14px;font-weight:700;color:var(--white)}
.nav{position:absolute;top:45px;left:439px;display:flex;align-items:center;height:39px}
.nav a{font-size:21px;font-weight:700;color:var(--yellow);text-decoration:none;text-transform:uppercase;margin-right:22px;line-height:39px}
.nav a.active{background:var(--yellow);color:var(--ink);padding:0 10px}
.nav .user{width:38px;height:38px;border:2px solid var(--white);background:#222;display:flex;align-items:flex-end;justify-content:center;margin:0 10px 0 4px}
.nav .login{color:var(--yellow);font-size:19px;font-weight:700;text-transform:none}
.headline{position:absolute;left:0;top:200px;width:1200px;text-align:center;color:var(--white);font-weight:700;text-shadow:0 2px 4px rgba(0,0,0,.35)}
.headline .l1{font-size:33px;line-height:42px}
.headline .l2{font-size:28px;line-height:40px}
.hl{color:var(--yellow)}
.search{position:absolute;left:320px;top:493px;width:562px;height:57px;display:flex}
.search-field{flex:1;background:var(--white);font-size:32px;color:#c8c8c8;padding:8px 8px;line-height:41px}
.search-btn{width:68px;background:var(--yellow);display:flex;align-items:center;justify-content:center}
.all-courses{position:absolute;left:0;top:556px;width:1200px;text-align:center;font-size:23px;font-weight:700;color:var(--yellow);text-decoration:underline}

/* features */
.features{position:absolute;left:0;top:700px;width:1200px;height:323px;background:var(--band-grey)}
.feature{position:absolute;top:52px;width:220px;text-align:center}
.feature-icon{width:109px;height:109px;border-radius:50%;background:var(--white);margin:0 auto;display:flex;align-items:center;justify-content:center}
.feature h3{font-size:21px;font-weight:700;color:var(--ink);margin-top:14px}
.feature p{font-size:13px;line-height:18px;color:var(--ink);margin-top:16px}

/* latest courses */
.section-title{position:absolute;left:0;width:1200px;text-align:center;font-family:"Lato",sans-serif;font-weight:900;font-size:31px;color:var(--ink)}
.carousel-arrow{position:absolute;top:1120px;width:28px;height:28px;border:2px solid var(--ink);border-radius:5px;display:flex;align-items:center;justify-content:center;background:var(--white)}
.card{position:absolute;top:1157px;width:224px;height:402px;border:1px solid var(--line);background:var(--white)}
.card-cover{height:220px;background:linear-gradient(160deg,#f9cf3e,#f3b614)}
.card-title{font-size:17px;line-height:19px;text-align:center;color:var(--ink);margin-top:12px;height:40px;text-transform:uppercase;padding:0 6px}
.card-meta{display:flex;align-items:center;justify-content:space-between;padding:0 10px;margin-top:6px;font-size:13px;color:var(--muted)}
.stars{display:flex;gap:2px;align-items:center}
.card-row{display:flex;justify-content:space-between;align-items:center;padding:0 10px;margin-top:8px;font-size:10px;color:var(--muted)}
.price{font-size:20px;font-weight:700;color:var(--ink)}
.card-author{border-top:2px solid var(--yellow);margin-top:8px;display:flex;align-items:center;gap:10px;padding:6px 8px}
.author-thumb{width:42px;height:42px;background:linear-gradient(135deg,#4a4a4a,#8a6b55)}
.author-name{font-size:16px;font-weight:700;color:var(--ink);line-height:18px}
.author-role{font-size:13px;font-style:italic;color:var(--ink)}
.btn-outline{position:absolute;left:489px;top:1589px;width:211px;height:54px;border:2px solid var(--ink);display:flex;align-items:center;justify-content:center;font-size:18px;color:var(--ink)}

/* dark info band */
.info-band{position:absolute;left:0;top:1666px;width:1200px;height:493px;background:var(--dark)}
.col-title{position:absolute;top:1704px;font-size:23px;font-weight:700;color:var(--white)}
.news-item{position:absolute;left:120px;width:300px;height:72px;background:var(--white);border-bottom:5px solid var(--yellow);display:flex;align-items:center;gap:14px;padding-left:12px}
.news-thumb{width:44px;height:44px;background:linear-gradient(135deg,#f6c22a,#e8a90f)}
.news-title{font-size:14px;font-weight:700;color:#666;line-height:15px;text-transform:uppercase}
.news-date{font-size:15px;color:var(--ink);margin-top:2px}
.field{position:absolute;left:470px;width:262px;background:var(--white);font-size:20px;color:#cfcfcf;padding:2px 6px}
.join{position:absolute;left:643px;top:1982px;width:89px;height:34px;background:var(--yellow);color:var(--ink);font-size:24px;font-weight:700;display:flex;align-items:center;justify-content:center}
.form-note{position:absolute;left:462px;top:2040px;width:280px;text-align:center;font-size:13px;line-height:16px;color:var(--white)}
.instructor{position:absolute;left:770px;top:1755px;width:310px;height:356px;background:var(--white);text-align:center}
.instructor-photo{width:136px;height:136px;border-radius:50%;margin:18px auto 0;background:radial-gradient(circle at 50% 40%,#9a7a62,#3a2c24);border:3px solid var(--yellow)}
.instructor-name{font-size:25px;color:var(--yellow);margin-top:12px}
.instructor-role{font-size:20px;font-weight:700;color:var(--ink);margin-top:2px}
.instructor-text{font-size:13px;line-height:16px;color:var(--ink);margin:10px auto 0;width:190px}
.btn-yellow{position:absolute;left:69px;top:306px;width:175px;height:50px;background:var(--yellow);font-size:16px;color:var(--ink);display:flex;align-items:center;justify-content:center;text-transform:uppercase}

/* testimonial */
.quote{position:absolute;left:180px;top:2240px;width:840px;text-align:center;font-size:16px;line-height:24px;font-style:italic;color:#777;text-transform:uppercase}
.student-photo{position:absolute;left:525px;top:2298px;width:150px;height:150px;border-radius:50%;border:3px solid var(--yellow);background:radial-gradient(circle at 50% 40%,#e9c9ad,#8a5a3c)}
.student-name{position:absolute;left:0;top:2458px;width:1200px;text-align:center;font-size:15px;font-weight:700;font-style:italic;color:var(--yellow);text-transform:uppercase}
.dot{position:absolute;top:2511px;width:18px;height:18px;border-radius:50%;background:#cfcfcf}
.dot.on{background:var(--yellow)}

/* social + footer */
.social{position:absolute;left:0;top:2557px;width:1200px;height:95px;background:var(--darker)}
.social-item{position:absolute;top:20px;display:flex;align-items:center;gap:10px}
.social-mark{width:46px;height:46px;background:var(--yellow)}
.social-label{font-size:18px;font-weight:700;color:var(--white);line-height:22px}
.social-count{display:inline-block;background:var(--ink);color:var(--white);font-size:18px;font-weight:700;padding:0 6px;line-height:26px}
.footer{position:absolute;left:0;top:2652px;width:1200px;height:75px;background:var(--footer);text-align:center}
.footer-links{margin-top:13px;font-size:17px;color:var(--ink);word-spacing:2px}
.footer-links span{margin:0 8px}
.copyright{font-size:15px;font-weight:700;color:var(--ink);margin-top:4px}
</style>
</head>
<body>

<header class="hero">
  <div class="hero-photo" role="img" aria-label="Photo from above of two students studying with a laptop on a wooden bench"></div>
  <div class="brand"><span class="brand-dot"></span><span class="brand-name">Brivora</span></div>
  <div class="brand-tag">Courses that Work</div>
  <nav class="nav">
    <a class="active">Home</a>
    <a>Courses</a>
    <a>About</a>
    <a>Contact</a>
    <span class="user"><svg width="26" height="30" viewBox="0 0 26 30"><circle cx="13" cy="10" r="7" fill="#fff"/><path d="M1 30c0-8 5-12 12-12s12 4 12 12z" fill="#fff"/></svg></span>
    <a class="login">Login | Register</a>
  </nav>
  <div class="headline">
    <div class="l1">Facilitating Elegant <span class="hl">E-LEARNING</span> &amp; Mixed Learning</div>
    <div class="l2">Solutions For <span class="hl">INDIVIDUALS</span>, Colleges, Organisations</div>
    <div class="l2">&amp; <span class="hl">B2B</span>.</div>
  </div>
  <div class="search">
    <div class="search-field">Search...</div>
    <div class="search-btn"><svg width="34" height="34" viewBox="0 0 34 34"><circle cx="14" cy="14" r="10" fill="none" stroke="#fff" stroke-width="4"/><line x1="21" y1="21" x2="31" y2="31" stroke="#fff" stroke-width="4" stroke-linecap="round"/></svg></div>
  </div>
  <div class="all-courses">View All Courses &gt;&gt;</div>
</header>

<section class="features">
  <div class="feature" style="left:113px">
    <div class="feature-icon"><svg width="56" height="56" viewBox="0 0 24 24"><path d="M12 2l3 6.5 7 .8-5.2 4.8 1.5 7L12 17.6 5.7 21.1l1.5-7L2 9.3l7-.8z" fill="var(--yellow)"/></svg></div>
    <h3>Great Material</h3>
    <p>Lorem ipsum dolor sit amet, con-<br>sectetur adipiscing elit, sed do<br>eiusmod tempor incididunt.</p>
  </div>
  <div class="feature" style="left:365px">
    <div class="feature-icon"><svg width="60" height="56" viewBox="0 0 60 56"><circle cx="22" cy="32" r="13" fill="none" stroke="var(--yellow)" stroke-width="7" stroke-dasharray="5 3"/><circle cx="22" cy="32" r="5" fill="var(--yellow)"/><circle cx="44" cy="14" r="9" fill="none" stroke="var(--yellow)" stroke-width="5" stroke-dasharray="4 2.5"/><circle cx="47" cy="42" r="7" fill="none" stroke="var(--yellow)" stroke-width="4" stroke-dasharray="3 2"/></svg></div>
    <h3>High Quality</h3>
    <p>Lorem ipsum dolor sit amet, con-<br>sectetur adipiscing elit, sed do<br>eiusmod tempor incididunt.</p>
  </div>
  <div class="feature" style="left:613px">
    <div class="feature-icon"><svg width="56" height="50" viewBox="0 0 24 22"><path d="M12 21S1 14 1 7a5.5 5.5 0 0 1 11-1 5.5 5.5 0 0 1 11 1c0 7-11 14-11 14z" fill="var(--yellow)"/></svg></div>
    <h3>Learning is Fun</h3>
    <p>Lorem ipsum dolor sit amet, con-<br>sectetur adipiscing elit, sed do<br>eiusmod tempor incididunt.</p>
  </div>
  <div class="feature" style="left:863px">
    <div class="feature-icon"><svg width="58" height="52" viewBox="0 0 58 52"><path d="M4 28l8-8 12 12L50 2l6 8-32 40z" fill="var(--yellow)"/></svg></div>
    <h3>It’s Simple</h3>
    <p>Lorem ipsum dolor sit amet, con-<br>sectetur adipiscing elit, sed do<br>eiusmod tempor incididunt.</p>
  </div>
</section>

<h2 class="section-title" style="top:1059px">LATEST <span class="hl">COURSES</span></h2>
<div class="carousel-arrow" style="left:1016px"><svg width="12" height="14" viewBox="0 0 12 14"><path d="M8 2L3 7l5 5" fill="none" stroke="#1b1b1b" stroke-width="2.5"/></svg></div>
<div class="carousel-arrow" style="left:1047px"><svg width="12" height="14" viewBox="0 0 12 14"><path d="M4 2l5 5-5 5" fill="none" stroke="#1b1b1b" stroke-width="2.5"/></svg></div>

<article class="card" style="left:120px">
  <div class="card-cover" role="img" aria-label="Yellow course cover for Quick Fennish Fundamentals"></div>
  <div class="card-title">Quick Fennish<br>Fundamentals Suite</div>
  <div class="card-meta"><span class="stars"><svg width="82" height="16" viewBox="0 0 82 16"><g fill="#f7c125"><path id="s" d="M8 0l2.4 5 5.6.6-4.2 3.8 1.2 5.6L8 12.2 3 15l1.2-5.6L0 5.6 5.6 5z"/><use href="#s" x="16.5"/><use href="#s" x="33"/></g><g fill="#cfcfcf"><use href="#s" x="49.5"/><use href="#s" x="66"/></g></svg></span><span>( 3 REVIEWS )</span></div>
  <div class="card-row"><span>▤ 10 LESSONS</span><span class="price">$199</span></div>
  <div class="card-author"><div class="author-thumb" role="img" aria-label="Instructor portrait"></div><div><div class="author-name">Harold Wen Pike</div><div class="author-role">Language Expert, Trainer</div></div></div>
</article>
<article class="card" style="left:368px">
  <div class="card-cover" role="img" aria-label="Yellow course cover for Quick Fennish plus Fennish Nibbles bundle"></div>
  <div class="card-title">Quick Fennish + Fennish<br>Nibbles Bundle</div>
  <div class="card-meta"><span class="stars"><svg width="82" height="16" viewBox="0 0 82 16"><g fill="#cfcfcf"><use href="#s"/><use href="#s" x="16.5"/><use href="#s" x="33"/><use href="#s" x="49.5"/><use href="#s" x="66"/></g></svg></span><span>( 0 REVIEWS )</span></div>
  <div class="card-row"><span>▤ 30 LESSONS</span><span class="price">$159</span></div>
  <div class="card-author"><div class="author-thumb" role="img" aria-label="Instructor portrait"></div><div><div class="author-name">Harold Wen Pike</div><div class="author-role">Language Expert, Trainer</div></div></div>
</article>
<article class="card" style="left:614px">
  <div class="card-cover" role="img" aria-label="Yellow course cover for Fennish Nibbles"></div>
  <div class="card-title">Fennish Nibbles</div>
  <div class="card-meta"><span class="stars"><svg width="82" height="16" viewBox="0 0 82 16"><g fill="#f7c125"><use href="#s"/><use href="#s" x="16.5"/><use href="#s" x="33"/><use href="#s" x="49.5"/></g><g fill="#cfcfcf"><use href="#s" x="66"/></g></svg></span><span>( 4 REVIEWS )</span></div>
  <div class="card-row"><span>▤ 15 LESSONS</span><span class="price">$15.99</span></div>
  <div class="card-author"><div class="author-thumb" role="img" aria-label="Instructor portrait"></div><div><div class="author-name">Harold Wen Pike</div><div class="author-role">Language Expert, Trainer</div></div></div>
</article>
<article class="card" style="left:861px">
  <div class="card-cover" role="img" aria-label="Yellow course cover for Quick Fennish Fundamentals bundle"></div>
  <div class="card-title">Quick Fennish<br>Fundamentals Suite</div>
  <div class="card-meta"><span class="stars"><svg width="82" height="16" viewBox="0 0 82 16"><g fill="#f7c125"><use href="#s"/><use href="#s" x="16.5"/><use href="#s" x="33"/></g><g fill="#cfcfcf"><use href="#s" x="49.5"/><use href="#s" x="66"/></g></svg></span><span>( 3 REVIEWS )</span></div>
  <div class="card-row"><span>▤ 10 LESSONS</span><span class="price">$199</span></div>
  <div class="card-author"><div class="author-thumb" role="img" aria-label="Instructor portrait"></div><div><div class="author-name">Harold Wen Pike</div><div class="author-role">Language Expert, Trainer</div></div></div>
</article>
<div class="btn-outline">VIEW MORE COURSES</div>

<section class="info-band"></section>
<div class="col-title" style="left:132px">NEWS <span class="hl">/ Up-Coming Courses</span></div>
<div class="col-title" style="left:464px">Your <span class="hl">Journey Start Here!</span></div>
<div class="col-title" style="left:770px">Featured <span class="hl">Instructor</span></div>

<div class="news-item" style="top:1764px"><div class="news-thumb" role="img" aria-label="Course thumbnail"></div><div><div class="news-title">Quick Fennish<br>Fundamentals Suite</div><div class="news-date">15 March 2015</div></div></div>
<div class="news-item" style="top:1855px"><div class="news-thumb" role="img" aria-label="Course thumbnail"></div><div><div class="news-title">Quick Fennish<br>Fundamentals Suite</div><div class="news-date">15 March 2015</div></div></div>
<div class="news-item" style="top:1945px"><div class="news-thumb" role="img" aria-label="Course thumbnail"></div><div><div class="news-title">Quick Fennish<br>Fundamentals Suite</div><div class="news-date">15 March 2015</div></div></div>
<div class="news-item" style="top:2034px"><div class="news-thumb" role="img" aria-label="Course thumbnail"></div><div><div class="news-title">Quick Fennish<br>Fundamentals Suite</div><div class="news-date">15 March 2015</div></div></div>

<div class="field" style="top:1764px;height:32px">Name</div>
<div class="field" style="top:1816px;height:32px">Email</div>
<div class="field" style="top:1868px;height:102px;font-size:15px">Reason/Description</div>
<div class="join">Join!</div>
<div class="form-note">*Brivora for Organisations and Academic<br>Institutes Coming Soon!</div>

<aside class="instructor">
  <div class="instructor-photo" role="img" aria-label="Portrait of instructor Harold Wen Pike"></div>
  <div class="instructor-name">Harold Wen Pike</div>
  <div class="instructor-role">Language Expert, Trainer</div>
  <div class="instructor-text">Lorem ipsum dolor sit amet, consecte-tur adipiscing elit, sed do eiusmod tempor incididunt.....</div>
  <div class="btn-yellow">View Profile</div>
</aside>

<h2 class="section-title" style="top:2192px">WHAT <span class="hl">STUDENT</span> SAY ?</h2>
<p class="quote">“Lorem ipsum dolor sit amet, consectetur adipiscing elit, sed do eiusmod tempor incididunt<br>ut labore et dolore magna aliqua.”</p>
<div class="student-photo" role="img" aria-label="Portrait of student Maren Tollby"></div>
<div class="student-name">Maren Tollby</div>
<span class="dot on" style="left:559px"></span>
<span class="dot" style="left:591px"></span>
<span class="dot" style="left:623px"></span>

<section class="social">
  <div class="social-item" style="left:362px"><span class="social-mark"></span><div><div class="social-label">Chirpline</div><span class="social-count">14,125</span></div></div>
  <div class="social-item" style="left:520px"><span class="social-mark"></span><div><div class="social-label">Leafbook</div><span class="social-count">10,319</span></div></div>
  <div class="social-item" style="left:676px"><span class="social-mark"></span><div><div class="social-label">Orbit +</div><span class="social-count">18,416</span></div></div>
</section>

<footer class="footer">
  <div class="footer-links"><span>About Us</span><span>Affiliates</span><span>Blog</span><span>Support</span><span>Contact Us</span><span>Careers</span><span>Terms of Use</span><span>Privacy Policy</span></div>
  <div class="copyright">Copyright © 2015 brivora-learn.test. All Rights Reserved</div>
</footer>

</body>
</html>
```